Serena Alba Candle Box Package Design

Two box sizes:
14oz Candle in a box Gift Boxes - 4 x 4 x 6
4oz Candle in a box Gift Boxes - 3 x 3 x 3
Website: www.serenaalba-example.com
IG: @serena.alba
My brand is a sophisticated brand with luxury candles made of coconut wax.  Serena Alba means bright life. Our candles represent hope and light.
You matter, you are worthy, powerful and beautiful!
Each candle is hand poured, vegan, environmentally conscious, uniquely scented and rooted in the importance of self care and community. We donate a percentage of our proceeds to organizations that seek to empower and enrich women.
At Serena Alba, we believe that positive energy can move mountains.
We strive to elevate that energy in every way possible. Our candles are handmade with confident positivity in mind - 100% vegan friendly, non-toxic and carefully crafted for optimal performance yet minimal impact on the environment.

```html
<!DOCTYPE html>
<html lang="en">
<head>
<meta charset="utf-8">
<title>Serena Alba – Candle Box Panels</title>
<link href="https://fonts.googleapis.com/css2?family=Italiana&family=Montserrat:wght@500&family=Poppins:wght@400&family=Sacramento&display=swap" rel="stylesheet">
<style>
  :root {
    --backdrop: #e4e4e4;
    --panel-top: #e6dfe0;
    --panel-bottom: #f1e8ea;
    --ink: #1e1a1b;
    --script-ink: #3b3335;
    --orchid-light: #f4b2dc;
    --orchid-mid: #e27ac0;
    --orchid-deep: #9e2050;
    --fold: #cfc4c7;
  }
  * { margin: 0; padding: 0; box-sizing: border-box; }
  html, body {
    width: 1200px; height: 1024px; overflow: hidden;
    background: var(--backdrop);
  }
  .canvas { position: relative; width: 1200px; height: 1024px; }

  .panel {
    position: absolute; width: 420px; height: 420px; overflow: hidden;
    background: linear-gradient(180deg, var(--panel-top), var(--panel-bottom));
    outline: 1px solid var(--fold);
  }
  .panel-top   { left: 600px; top: 92px; }
  .panel-side  { left: 180px; top: 512px; }
  .panel-front { left: 600px; top: 512px; }

  .panel-art { position: absolute; inset: 0; width: 100%; height: 100%; }

  .top-mark {
    position: absolute; left: 150px; top: 70px; width: 200px;
    text-align: center;
    font-family: "Italiana", serif; font-size: 30px; line-height: 1;
    letter-spacing: 1px; text-transform: uppercase; color: var(--ink);
  }

  .brand-block {
    position: absolute; left: 160px; top: 218px; width: 240px;
    text-align: center; color: var(--ink);
  }
  .brand-name {
    font-family: "Italiana", serif; font-weight: 400;
    font-size: 34px; line-height: 1; letter-spacing: 0.5px;
    text-transform: uppercase; white-space: nowrap;
  }
  .brand-tagline {
    display: flex; align-items: center; justify-content: center; gap: 8px;
    margin-top: 10px; white-space: nowrap;
    font-family: "Montserrat", sans-serif; font-size: 9px; font-weight: 500;
    letter-spacing: 3.5px; text-transform: uppercase;
  }
  .brand-tagline::before, .brand-tagline::after {
    content: ""; width: 16px; height: 1px; background: var(--ink);
  }
  .brand-script {
    margin-top: 2px;
    font-family: "Sacramento", cursive; font-size: 15px; color: var(--script-ink);
  }
  .net-weight {
    position: absolute; left: 186px; top: 370px;
    font-family: "Poppins", sans-serif; font-size: 10px; color: var(--ink);
  }
  .social-handle {
    position: absolute; left: 300px; top: 370px;
    display: flex; align-items: center; gap: 5px;
    font-family: "Poppins", sans-serif; font-size: 10px; color: var(--ink);
  }
  .social-handle .dot { width: 9px; height: 9px; border-radius: 50%; background: var(--ink); }
</style>
</head>
<body>
<main class="canvas">
  <svg width="0" height="0" aria-hidden="true" style="position:absolute">
    <defs>
      <radialGradient id="orchidBloom" cx="40%" cy="40%" r="70%">
        <stop offset="0%" stop-color="#f4b2dc"/>
        <stop offset="60%" stop-color="#e27ac0"/>
        <stop offset="100%" stop-color="#9e2050"/>
      </radialGradient>
    </defs>
  </svg>

  <section class="panel panel-top" aria-label="Box lid">
    <svg class="panel-art" viewBox="0 0 420 420" role="img"
         aria-label="Pink orchid blooms trailing across the upper-left and lower edge of the lid">
      <path fill="url(#orchidBloom)" d="M0 0 H150 C140 40 90 60 40 70 C20 120 10 170 0 200 Z"/>
      <path fill="url(#orchidBloom)" d="M60 300 C110 250 190 240 250 270 C300 300 360 280 420 300 V420 H40 C30 380 40 330 60 300 Z"/>
    </svg>
    <p class="top-mark">Serena Alba</p>
  </section>

  <section class="panel panel-side" aria-label="Box side">
    <svg class="panel-art" viewBox="0 0 420 420" role="img"
         aria-label="Repeating pattern of pink phalaenopsis orchids on dark stems covering the side panel">
      <rect width="420" height="420" fill="#e9dde3"/>
      <rect width="420" height="420" fill="url(#orchidBloom)" opacity="0.85"/>
    </svg>
  </section>

  <section class="panel panel-front" aria-label="Box front">
    <svg class="panel-art" viewBox="0 0 420 420" role="img"
         aria-label="Large pink orchid blooms spilling across the top and left of the front panel, with faint outline flowers behind">
      <path fill="url(#orchidBloom)"
        d="M0 0 H420 V40 C380 100 330 120 290 130 C250 140 230 170 190 160
           C150 160 130 180 130 220 C130 290 120 360 90 420 H0 Z"/>
    </svg>
    <div class="brand-block">
      <h1 class="brand-name">Serena Alba</h1>
      <p class="brand-tagline">Handmade Candles</p>
      <p class="brand-script">with purpose and love</p>
    </div>
    <p class="net-weight">14oz | 396g</p>
    <p class="social-handle"><span class="dot"></span>@serena.alba</p>
  </section>
</main>
</body>
</html>
```